Corvane Business Cards & Staionary
Corvane, Inc.
Project: Corvane Business Cards & Staionary
Corvane Business Cards & Staionary - Real Estate
Creative Brief
Professional
Leonard T. Haskovich
President
418 W. Thornberry Blvd. Ridgemont, TX 75204
len@corvanetx.com

```html
<!DOCTYPE html>
<html lang="en">
<head>
<meta charset="utf-8">
<title>Corvane, Inc. — Business Cards</title>
<link href="https://fonts.googleapis.com/css2?family=Cinzel:wght@400;600&display=swap" rel="stylesheet">
<style>
  :root {
    --backdrop: #c9c9c9;
    --paper: #ffffff;
    --gold: #d9a21c;
    --gold-light: #f0c24a;
    --gold-deep: #b07f10;
    --charcoal: #555659;
    --ink: #4a4b4e;
    --rule: #8a8b8e;
  }
  * { box-sizing: border-box; margin: 0; padding: 0; }
  html, body { width: 1200px; height: 895px; overflow: hidden; }
  body {
    background: var(--backdrop);
    font-family: "Cinzel", "Times New Roman", serif;
    color: var(--ink);
    position: relative;
  }
  .card {
    position: absolute;
    top: 293px;
    width: 540px;
    height: 309px;
    box-shadow: 0 6px 18px rgba(0,0,0,.22);
    overflow: hidden;
  }

  /* Front card */
  .card-front { left: 40px; background: var(--paper); }
  .brand {
    position: absolute; top: 38px; left: 0; right: 0;
    text-align: center;
  }
  .brand-name {
    display: inline-flex; align-items: center; gap: 10px;
    font-size: 34px; font-weight: 600; color: var(--charcoal);
    letter-spacing: 1px;
  }
  .brand-mark { width: 14px; height: 14px; background: var(--gold); }
  .brand-tagline {
    margin-top: 4px;
    font-size: 7px; letter-spacing: 1.4px; color: var(--charcoal);
    text-transform: uppercase;
  }
  .name-band {
    position: absolute; top: 126px; left: 0; right: 0; height: 30px;
    background: linear-gradient(90deg, var(--gold-deep), var(--gold-light) 50%, var(--gold-deep));
    border-top: 3px solid var(--paper);
    border-bottom: 3px solid var(--paper);
    box-shadow: 0 -2px 0 var(--rule), 0 2px 0 var(--rule);
    display: flex; align-items: center; justify-content: center;
    color: var(--paper); font-size: 12px; letter-spacing: 1.2px;
  }
  .name-band .role { margin-left: 6px; }
  .contacts {
    position: absolute; top: 186px; left: 40px; right: 40px;
    display: grid; grid-template-columns: 1fr auto; row-gap: 10px; column-gap: 20px;
    list-style: none;
    font-size: 10.5px; letter-spacing: .6px; color: var(--ink);
  }
  .contacts li { display: flex; align-items: center; gap: 8px; white-space: nowrap; }
  .contacts .right { justify-self: start; }
  .contact-icon { width: 14px; height: 14px; flex: none; }

  /* Back card */
  .card-back {
    left: 620px;
    background: radial-gradient(ellipse at 60% 40%, var(--gold-light), var(--gold) 55%, var(--gold-deep));
  }
  .back-brand {
    position: absolute; top: 112px; left: 60px;
    display: flex; align-items: center; gap: 12px;
    font-size: 40px; font-weight: 600; color: var(--charcoal);
    letter-spacing: 1px;
  }
  .back-brand .brand-mark { width: 18px; height: 18px; background: var(--paper); }
  .back-web {
    position: absolute; right: 34px; bottom: 36px;
    font-size: 13px; letter-spacing: 2.5px; color: var(--charcoal);
  }
</style>
</head>
<body>

<section class="card card-front" aria-label="Business card front">
  <div class="brand">
    <div class="brand-name"><span class="brand-mark"></span>Corvane, Inc.</div>
    <p class="brand-tagline">Residential Property Management Group</p>
  </div>

  <div class="name-band">
    <span class="person">Leonard T. Haskovich</span>
    <span class="role">| President</span>
  </div>

  <ul class="contacts">
    <li>
      <svg class="contact-icon" viewBox="0 0 14 14" aria-hidden="true"><circle cx="7" cy="7" r="7" fill="var(--gold)"/><path d="M7 3a2.4 2.4 0 0 0-2.4 2.4C4.6 7.3 7 10.5 7 10.5s2.4-3.2 2.4-5.1A2.4 2.4 0 0 0 7 3z" fill="#fff"/></svg>
      418 W. Thornberry Blvd. Ridgemont, TX 75204
    </li>
    <li class="right">
      <svg class="contact-icon" viewBox="0 0 14 14" aria-hidden="true"><circle cx="7" cy="7" r="7" fill="var(--gold)"/><path d="M4.5 3.5l1.4 0 .6 1.8-.9.7a5 5 0 0 0 2.4 2.4l.7-.9 1.8.6v1.4c-3.4.2-6.2-2.6-6-6z" fill="#fff"/></svg>
      (972) 555-0172
    </li>
    <li>
      <svg class="contact-icon" viewBox="0 0 14 14" aria-hidden="true"><circle cx="7" cy="7" r="7" fill="var(--gold)"/><path d="M4.5 3.5l1.4 0 .6 1.8-.9.7a5 5 0 0 0 2.4 2.4l.7-.9 1.8.6v1.4c-3.4.2-6.2-2.6-6-6z" fill="#fff"/></svg>
      (972) 555-0148
    </li>
    <li class="right">
      <svg class="contact-icon" viewBox="0 0 14 14" aria-hidden="true"><circle cx="7" cy="7" r="7" fill="var(--gold)"/><circle cx="7" cy="7" r="3.6" fill="none" stroke="#fff" stroke-width="1"/><path d="M3.4 7h7.2M7 3.4c-1.6 2.2-1.6 5 0 7.2M7 3.4c1.6 2.2 1.6 5 0 7.2" fill="none" stroke="#fff" stroke-width=".8"/></svg>
      www.corvanetx.com
    </li>
    <li>
      <svg class="contact-icon" viewBox="0 0 14 14" aria-hidden="true"><circle cx="7" cy="7" r="7" fill="var(--gold)"/><rect x="3.6" y="4.6" width="6.8" height="4.8" fill="#fff"/><path d="M3.6 4.6L7 7.3l3.4-2.7" fill="none" stroke="var(--gold)" stroke-width=".8"/></svg>
      len@corvanetx.com
    </li>
  </ul>
</section>

<section class="card card-back" aria-label="Business card back">
  <div class="back-brand"><span class="brand-mark"></span>Corvane</div>
  <p class="back-web">www.corvanetx.com</p>
</section>

</body>
</html>
```